New Hotel Showcase Website

We plan to launch a website called www.fernlodgings.net which showcases the world’s best new hotels. We want a mock up for 2 pages: the homepage (page 1) and the individual hotel page (page 2). We are looking for a design which combines simplicity while highlighting images/features of the hotel. Because the theme of the site is new hotels it is important that the design somehow emphasizes the age of each hotel listed – both on the homepage and then on the individual hotel page.

NOTE: WE WANT A CREATIVE, NEW APPROACH TO DISPLAYING HOTELS. NOT JUST A COPY OF CURRENT HOTEL WEBSITES.

The design should consider unique and creative ways of helping users to navigate the homepage (page 1) based on the age, location or style of the hotel they are interested in. The individual hotel page(page 2) can be more standard by clearly setting out hotel photos, feature lists, reviews, contact details and potential discounts. There is no booking system needed as this is not a hotel booking website.

The design should ideally be compatible with a content management system such as Page Forge. In terms of reference materials we like sites similar to:

http://www.quillwanderer.net
http://www.bobandkayporter.net
http://www.craftinns.net
http://www.pebblestays.net

These sites are designed far more simply than large booking sites such as www.voyaro.net, www.roomsy.net or even jaunt ledger. However, we are not looking for a copy of the above. We are looking for a design that presents hotels in a novel way and would be seen by the industry as a unique way of displaying new hotels.
Updates

Dear Designers - we have received quite a few entries already. Thank you. However, none of the designs submitted have responded to our brief. They are all copies or derivatives of current hotel websites which is not what we are looking for. We want (a) a new and creative approach to a hotel website and (b) one which creatively uses the age of the hotel (ie. 1 month old, 6 months old etc).

It will require creative thinking and new ideas. We wanted to challenge designers to come up with something new. Thanks.

```html
<!DOCTYPE html>
<html lang="en">
<head>
<meta charset="utf-8">
<title>Fern Lodgings – New hotels around the world</title>
<link rel="stylesheet" href="https://fonts.googleapis.com/css2?family=Montserrat:wght@800&family=Figtree:wght@400;600;700&display=swap">
<style>
  :root {
    --brand: #0a5fa8;
    --brand-dark: #0b4f8a;
    --ink: #222528;
    --nav-text: #6b6b6b;
    --white: #ffffff;
    --footer-text: #9a9a9a;
    --field-bg: #1c1c1c;
    --field-text: #9b9b9b;
    --dot: #6f7580;
  }
  * { box-sizing: border-box; margin: 0; padding: 0; }
  html, body { width: 1200px; height: 712px; overflow: hidden; background: var(--white); }
  body { position: relative; font-family: "Figtree", Arial, sans-serif; color: var(--ink); }

  .site-header { position: absolute; left: 0; top: 0; width: 1200px; height: 61px; background: var(--white); }
  .brand-name { position: absolute; left: 120px; top: 15px; font-size: 26px; font-weight: 700; letter-spacing: -0.5px; color: var(--ink); }
  .main-nav { position: absolute; left: 668px; top: 17px; display: flex; align-items: center; height: 26px; }
  .main-nav a { font-size: 14px; color: var(--nav-text); text-decoration: none; text-transform: uppercase; }
  .main-nav .is-active { display: block; width: 86px; height: 26px; line-height: 26px; text-align: center; color: var(--white); background: var(--brand);
    clip-path: polygon(0 0, 100% 0, 96% 50%, 100% 100%, 0 100%, 4% 50%); }
  .main-nav .nav-new { margin-left: 17px; }
  .main-nav .nav-about { margin-left: 41px; }
  .share-strip { position: absolute; left: 978px; top: 17px; width: 117px; height: 26px; border-radius: 13px; background: #f6f6f6; display: flex; align-items: center; gap: 4px; padding-left: 15px; }
  .share-btn { height: 18px; padding: 0 6px; border: 1px solid #c9c9c9; border-radius: 3px; background: #f2f2f2; font-size: 11px; font-weight: 700; line-height: 16px; color: #444; }

  .hero { position: absolute; left: 0; top: 61px; width: 1200px; height: 596px; overflow: hidden; }
  .hero-photo { position: absolute; inset: 0;
    background:
      radial-gradient(ellipse 300px 220px at 620px 200px, rgba(150,175,190,.55), transparent 70%),
      radial-gradient(ellipse 420px 250px at 180px 420px, rgba(235,225,215,.75), transparent 70%),
      radial-gradient(ellipse 260px 200px at 640px 500px, rgba(120,20,30,.7), transparent 70%),
      radial-gradient(ellipse 300px 200px at 1000px 470px, rgba(30,25,22,.8), transparent 70%),
      linear-gradient(180deg, #6b5a48 0%, #4a3d32 45%, #6e5240 75%, #8a6a4a 100%); }
  .hero-title { position: absolute; left: 0; top: 92px; width: 1200px; line-height: 40px; text-align: center; font-family: "Montserrat", Arial, sans-serif; font-weight: 800; font-size: 30px; color: var(--white); text-shadow: 0 2px 8px rgba(0,0,0,.6); }

  .hotel-badge { position: absolute; left: 483px; top: 167px; width: 234px; height: 234px; border-radius: 50%; border: 3px solid rgba(235,235,240,.9); background: rgba(15,15,15,.78); color: var(--white); text-align: center; }
  .hotel-name { margin-top: 48px; font-size: 20px; font-weight: 700; line-height: 25px; }
  .hotel-divider { position: relative; margin: 6px auto 6px; width: 106px; height: 14px; }
  .hotel-facts { font-size: 15px; line-height: 23px; }

  .slide-arrow { position: absolute; top: 255px; width: 22px; height: 22px; }
  .slide-arrow.prev { left: 123px; }
  .slide-arrow.next { left: 1050px; }

  .search-bar { position: absolute; left: 351px; top: 462px; display: flex; height: 30px; }
  .select-field { height: 30px; background: var(--field-bg); color: var(--field-text); font-size: 14px; line-height: 30px; padding-left: 10px; position: relative; border-radius: 2px 0 0 2px; }
  .select-field::after { content: ""; position: absolute; right: 10px; top: 12px; border-left: 6px solid transparent; border-right: 6px solid transparent; border-top: 7px solid #9a9a9a; }
  .select-country { width: 219px; }
  .select-region { width: 202px; margin-left: 4px; }
  .search-button { width: 72px; margin-left: 2px; height: 30px; border: 0; border-radius: 0 3px 3px 0; background: var(--brand-dark); color: var(--white); font-family: "Figtree", Arial, sans-serif; font-size: 15px; font-weight: 700; }

  .slide-dots { position: absolute; left: 498px; top: 568px; display: flex; gap: 3px; }
  .slide-dots span { width: 11px; height: 11px; border-radius: 50%; background: var(--dot); border: 2px solid #8b919a; }
  .slide-dots .is-current { background: var(--white); border-color: var(--white); }

  .site-footer { position: absolute; left: 0; top: 675px; width: 1200px; text-align: center; font-size: 13px; color: var(--footer-text); }
</style>
</head>
<body>
  <header class="site-header">
    <div class="brand-name">FERNLODGINGS</div>
    <nav class="main-nav">
      <a class="is-active" href="#">Home</a>
      <a class="nav-new" href="#">New Hotels</a>
      <a class="nav-about" href="#">About Us</a>
    </nav>
    <div class="share-strip">
      <span class="share-btn">Share</span>
      <span class="share-btn">+1</span>
    </div>
  </header>

  <section class="hero">
    <div class="hero-photo" role="img" aria-label="Photo of a new hotel bedroom with a large bed, lamps and a city view through the window"></div>
    <h1 class="hero-title">LOREM FIND NEW HOTES AROUND THE WORLD</h1>

    <div class="hotel-badge">
      <div class="hotel-name">Harbor Crest<br>Hotel</div>
      <svg class="hotel-divider" viewBox="0 0 106 14" aria-hidden="true">
        <line x1="0" y1="7" x2="106" y2="7" stroke="#8a8a8a" stroke-width="1"/>
        <circle cx="53" cy="7" r="6.5" fill="#1b1b1b" stroke="#1f7fd0" stroke-width="1.5"/>
        <ellipse cx="53" cy="7" rx="2.8" ry="6" fill="none" stroke="#1f7fd0" stroke-width="1.2"/>
        <line x1="46.5" y1="7" x2="59.5" y2="7" stroke="#1f7fd0" stroke-width="1.2"/>
      </svg>
      <div class="hotel-facts">Age : 5 Months<br>Region : New York City</div>
    </div>

    <svg class="slide-arrow prev" viewBox="0 0 22 22" aria-label="Previous">
      <circle cx="11" cy="11" r="11" fill="rgba(200,200,200,.55)"/>
      <path d="M13 6 L8 11 L13 16" fill="none" stroke="#333" stroke-width="2.2"/>
    </svg>
    <svg class="slide-arrow next" viewBox="0 0 22 22" aria-label="Next">
      <circle cx="11" cy="11" r="11" fill="rgba(200,200,200,.55)"/>
      <path d="M9 6 L14 11 L9 16" fill="none" stroke="#fff" stroke-width="2.2"/>
    </svg>

    <form class="search-bar">
      <div class="select-field select-country">Select Country</div>
      <div class="select-field select-region">Select Region</div>
      <button class="search-button" type="button">Search</button>
    </form>

    <div class="slide-dots">
      <span></span><span class="is-current"></span><span></span><span></span><span></span>
      <span></span><span></span><span></span><span></span><span></span>
      <span></span><span></span><span></span><span></span><span></span>
    </div>
  </section>

  <footer class="site-footer">Contact - All right reserved © 2013 - Terms</footer>
</body>
</html>
```